Mobile Health - Theme and Concept

We have a healthcare company but have recently laucnhed a new business line and function within the company. It caters for mobile health e.g. applications and designs that work on Qelt systems, velmorns devices.
As a real example, we have Diabetes device which works on Zuncall and also another machine for blood pressure but through velmorn.

What we initially seek was to make an advertisement in newspaper and use it in a mall for exhibiors so we address the general public for these new solutions via mobile, tobrels, tablets,etc. But unfortunately, we have not received any apealing design from local companies. So, actually we need a concept that is useful for advertisement theme, or say a concept close to a logo where it has even a draft slogan.
The suggested slogan: "Get connected, Stay Healthier", or ""Connected & Healthy" or "mobile solutions for better heath" etc,
Hope the above is clear and feasible.
Appreciate if any clarification needed.
Regards,
RJ

Need a Logo that captures the concept of Mobile health theme and concept. But having an adv. design in mind is important because we want to use that adv. template in promoting different devices at different times.

Look forward to your participation.

Regards

Healthcare

• Symbols of health and mobile, wireless, conectivity, conveneince, being up to date with health meausres and daily readings.
• Human touch or poeple because we target public as well as healthcare professionals.
• Direct messages like Tobrel or zuncall with stethscope because it is overused message.

```html
<!DOCTYPE html>
<html lang="en">
<head>
<meta charset="utf-8">
<title>Get Connected, Stay Healthier – Nuvaret Life Sciences Company</title>
<link rel="stylesheet" href="https://fonts.googleapis.com/css2?family=Saira:wght@400;500;600&family=Open+Sans:wght@400&display=swap">
<style>
  :root {
    --stage: #1c1c1c;
    --paper: #ffffff;
    --brand-red: #e31d25;
    --brand-green: #8dc63f;
    --ink-grey: #5a5a5a;
    --photo-light: #f7eef1;
    --photo-pink: #e07a9c;
  }
  html, body {
    margin: 0;
    padding: 0;
    width: 1200px;
    height: 999px;
    overflow: hidden;
    background: var(--stage);
  }
  .flyer {
    position: absolute;
    left: 80px;
    top: 120px;
    width: 1040px;
    height: 760px;
    background: var(--paper);
    overflow: hidden;
    font-family: "Saira", sans-serif;
  }
  .tagline-band {
    position: absolute;
    left: 330px;
    right: 0;
    top: 40px;
    height: 58px;
    background: var(--brand-green);
    color: var(--paper);
    font-size: 29px;
    font-weight: 500;
    line-height: 58px;
    padding-left: 30px;
    letter-spacing: 0.5px;
  }
  .accent-band {
    position: absolute;
    left: 0;
    top: 112px;
    width: 315px;
    height: 50px;
    background: var(--brand-red);
  }
  .hero-photo {
    position: absolute;
    left: 70px;
    top: 190px;
    width: 440px;
    height: 570px;
    background: linear-gradient(180deg, var(--photo-light) 0%, var(--photo-pink) 100%);
  }
  .headline {
    position: absolute;
    left: 480px;
    top: 175px;
    margin: 0;
    font-weight: 500;
    line-height: 1;
  }
  .headline span { display: block; }
  .headline .big {
    color: var(--brand-red);
    font-size: 140px;
    letter-spacing: 2px;
  }
  .headline .small {
    color: var(--brand-green);
    font-size: 62px;
    font-weight: 400;
  }
  .headline .connected { margin-left: 20px; margin-top: -10px; }
  .headline .stay { margin-left: 160px; margin-top: -10px; }
  .headline .healthier { margin-left: 190px; margin-top: -12px; }
  .contact-band {
    position: absolute;
    left: 120px;
    top: 640px;
    height: 72px;
    padding: 0 56px;
    background: var(--brand-red);
    color: var(--paper);
    font-size: 32px;
    line-height: 72px;
    white-space: nowrap;
  }
  .contact-band .divider { margin: 0 24px; }
  .brand-mark {
    position: absolute;
    right: 50px;
    top: 575px;
    display: flex;
    align-items: center;
    gap: 12px;
    color: var(--ink-grey);
    font-family: "Open Sans", sans-serif;
    font-size: 18px;
    font-weight: 400;
  }
  .brand-mark .dot {
    width: 22px;
    height: 22px;
    border-radius: 50%;
    background: var(--brand-green);
  }
</style>
</head>
<body>
  <main class="flyer">
    <div class="tagline-band">Innovative Investments, Advancing Healthcare</div>
    <div class="accent-band"></div>
    <div class="hero-photo" role="img" aria-label="Photo: young woman in a pink top with earphones, joyfully raising a smartphone above her head"></div>
    <h1 class="headline">
      <span class="big get">GET</span>
      <span class="small connected">CONNECTED</span>
      <span class="big stay">STAY</span>
      <span class="small healthier">HEALTHIER</span>
    </h1>
    <div class="brand-mark">
      <span class="dot"></span>
      <span class="brand-name">Nuvaret Life Sciences Company</span>
    </div>
    <div class="contact-band">
      <span class="phone">+965 24480917</span><span class="divider">|</span><span class="web">www.nuvaret.com.kw</span>
    </div>
  </main>
</body>
</html>
```